Pull Up Sign for Financial Services Business

Looking to design a pull-up retractable banner for events. A design which I could add a second banner to so something that could flow across more than one banner would be ideal.

I have included my logo and business card so you can get an idea of colours and our branding style.

A disability image will be required on the banner. Dimensions are in image attached.

Target Market(s)

KAPR (Disability) Participants

Industry/Entity Type

Disability/Finance

Font styles to use
Other font styles liked:
• Raleway

Requirements
Must have
• Disability Image - match our branding. Text in image uploaded

```html
<!DOCTYPE html>
<html lang="en">
<head>
<meta charset="utf-8">
<title>Harbour Plan Management – Pull Up Banner</title>
<link href="https://fonts.googleapis.com/css2?family=Raleway:wght@500;600;700&family=Oswald:wght@600&display=swap" rel="stylesheet">
<style>
  :root{
    --navy:#232636;
    --teal:#1b9a9a;
    --teal-bright:#11b5b5;
    --magenta:#b32b72;
    --purple:#6a2c83;
    --white:#ffffff;
    --ink:#2a2a33;
    --stage:#e4e4e4;
  }
  *{box-sizing:border-box;margin:0;padding:0}
  html,body{width:1200px;height:1117px;overflow:hidden;background:var(--stage)}
  .banner{
    position:absolute;left:385px;top:28px;width:430px;height:1060px;
    background:var(--white);overflow:hidden;
    font-family:"Raleway",sans-serif;
    box-shadow:0 4px 18px rgba(0,0,0,.12);
  }
  .banner-shapes{position:absolute;left:0;top:0}
  .brand{position:absolute;left:44px;top:58px;display:flex;flex-direction:column;gap:8px}
  .brand-square{width:48px;height:48px;background:var(--magenta)}
  .brand-name{color:var(--magenta);font-weight:700;font-size:19px;line-height:1.1;width:150px}
  .headline{position:absolute;left:57px;top:418px;font-weight:700;font-size:57px;line-height:56px;letter-spacing:-.5px}
  .headline .line-one{color:var(--white);display:block}
  .headline .line-two{color:var(--teal-bright);display:block}
  .subline{position:absolute;left:57px;top:540px;color:var(--white);font-weight:700;font-size:20px;line-height:21px;width:220px}
  .features{position:absolute;left:85px;top:0;list-style:none;color:var(--ink);font-weight:500;font-size:12.5px;line-height:15px}
  .features li{position:absolute;left:0;white-space:nowrap}
  .contact-phone{position:absolute;left:122px;top:966px;color:var(--white);font-family:"Oswald",sans-serif;font-weight:600;font-size:36px;line-height:46px;letter-spacing:-.5px;white-space:nowrap}
  .contact-web{position:absolute;left:54px;top:1022px;color:var(--white);font-weight:700;font-size:16px;white-space:nowrap}
</style>
</head>
<body>
<div class="banner">
  <svg class="banner-shapes" width="430" height="1060" viewBox="0 0 430 1060">
    <defs>
      <linearGradient id="photoTone" x1="0" y1="0" x2="1" y2="1">
        <stop offset="0" stop-color="#f4f2ef"/>
        <stop offset=".6" stop-color="#dcd6ce"/>
        <stop offset="1" stop-color="#9fc8c9"/>
      </linearGradient>
      <linearGradient id="roundTone" x1="0" y1="0" x2="1" y2="1">
        <stop offset="0" stop-color="#d9cfc4"/>
        <stop offset="1" stop-color="#8b6a4f"/>
      </linearGradient>
      <linearGradient id="tealSwoosh" x1="0" y1="0" x2="1" y2="0">
        <stop offset="0" stop-color="#0fb7b7"/>
        <stop offset="1" stop-color="#1a8f90"/>
      </linearGradient>
    </defs>
    <path class="panel-navy" d="M0 240 H430 V555 C330 590 170 620 0 615 Z" fill="var(--navy)"/>
    <path class="swoosh-magenta" d="M0 250 C70 320 180 360 320 350 C200 395 80 380 0 350 Z" fill="var(--magenta)"/>
    <path class="hero-photo" role="img" aria-label="Photograph: a carer smiling with a young person in a wheelchair in a bright room"
          d="M0 0 H430 V270 C380 320 260 348 160 335 C90 325 40 295 0 258 Z" fill="url(#photoTone)"/>
    <path d="M0 258 C40 295 90 325 160 335 C260 348 380 320 430 270" fill="none" stroke="var(--white)" stroke-width="5"/>
    <path class="swoosh-teal" d="M430 272 V385 C340 420 200 425 45 352 C200 378 340 360 430 272 Z" fill="url(#tealSwoosh)"/>

    <path class="feature-frame" d="M240 627 H70 Q57 627 57 640 V890 Q57 903 70 903 H373 Q386 903 386 890 V748"
          fill="none" stroke="var(--magenta)" stroke-width="2"/>

    <circle cx="324" cy="654" r="92" fill="var(--white)"/>
    <circle cx="324" cy="654" r="86" fill="var(--teal)"/>
    <circle class="round-photo" role="img" aria-label="Photograph: a support worker helping an older man use a laptop" cx="324" cy="654" r="77" fill="url(#roundTone)"/>

    <g class="feature-icons" fill="var(--white)" stroke="var(--teal)" stroke-width="1.6" stroke-linecap="round" stroke-linejoin="round">
      <g transform="translate(57 658)"><circle r="15"/><path d="M-5 -7 H4 V7 H-5 Z M-2 -3 H2 M-2 0 H2 M-2 3 H2" fill="none"/></g>
      <g transform="translate(57 692)"><circle r="15"/><circle cy="-2" r="5" fill="none"/><path d="M-8 7 H8" fill="none"/></g>
      <g transform="translate(57 726)"><circle r="15"/><path d="M-7 -1 A7 7 0 0 1 6 -3 M7 1 A7 7 0 0 1 -6 3 M6 -3 L7 -7 M-6 3 L-7 7" fill="none"/></g>
      <g transform="translate(57 760)"><circle r="15"/><circle r="7" fill="none"/><path d="M0 -4 V0 L3 2" fill="none"/></g>
      <g transform="translate(57 794)"><circle r="15"/><circle r="4" fill="none"/><path d="M0 -8 V-5 M0 5 V8 M-8 0 H-5 M5 0 H8" fill="none"/></g>
      <g transform="translate(57 828)"><circle r="15"/><path d="M-7 -5 H7 V7 H-7 Z M-7 -1 H7 M-3 -8 V-4 M3 -8 V-4" fill="none"/></g>
      <g transform="translate(57 868)"><circle r="15"/><path d="M-7 -7 H1 V1 H-7 Z M-3 -3 L-2 -2 M3 -1 L5 2 L8 -4" fill="none"/></g>
    </g>

    <path class="footer-magenta" d="M0 958 C90 918 200 900 310 903 C200 916 100 950 0 1008 Z" fill="var(--magenta)"/>
    <path class="footer-teal" d="M0 1030 C120 950 260 915 430 925 V1060 H0 Z" fill="var(--teal)"/>

    <g class="phone-icon" transform="translate(100 990)">
      <circle r="16" fill="var(--white)"/>
      <path d="M-7 -8 L-3 -9 L-1 -3 L-4 -1 C-2 3 1 5 3 5 L5 2 L10 4 L9 8 C0 10 -10 0 -7 -8 Z" fill="var(--teal)"/>
    </g>

    <circle class="partner-badge" cx="378" cy="985" r="44" fill="var(--white)"/>
    <circle cx="378" cy="985" r="39" fill="var(--purple)"/>
  </svg>

  <div class="brand">
    <span class="brand-square"></span>
    <span class="brand-name">Harbour Plan Management</span>
  </div>

  <h1 class="headline"><span class="line-one">your plan,</span><span class="line-two">your way</span></h1>
  <p class="subline">Australia wide plan management</p>

  <ul class="features">
    <li style="top:650px">Monthly statements</li>
    <li style="top:684px">Real time funding access</li>
    <li style="top:718px">Expense reimbursements</li>
    <li style="top:752px">Providers paid within 3 business days</li>
    <li style="top:786px">Invoices processed daily</li>
    <li style="top:820px">Your own personal dedicated plan manager</li>
    <li style="top:853px">Choice and control - use both registered and<br>unregistered providers</li>
  </ul>

  <p class="contact-phone">1300 482 615</p>
  <p class="contact-web">harbourplanmanagement.com.au</p>
</div>
</body>
</html>
```